Vornel Technologies business card design

We need a business card designed with our new logo. it would be great if the card could communicate it is a technology based company.

Target Market(s)

system integrators

Industry/Entity Type

technology, IOT

Contact Information for Business Card

Name, designation, Address, telephone number, email address

Requirements
Must have
• logo and company name
Nice to have
• something to do with technology

```html
<!DOCTYPE html>
<html lang="en">
<head>
<meta charset="utf-8">
<title>Vornel Technologies – Business Card</title>
<link href="https://fonts.googleapis.com/css2?family=Roboto:wght@400;500;700&display=swap" rel="stylesheet">
<style>
  :root {
    --orange: #f7941d;
    --orange-deep: #ec8a18;
    --charcoal: #3b3b3d;
    --ink: #222222;
    --paper: #ffffff;
    --backdrop: #ededed;
  }
  * { margin: 0; padding: 0; box-sizing: border-box; }
  html, body { width: 1200px; height: 896px; overflow: hidden; }
  body {
    background: var(--backdrop);
    font-family: "Roboto", Arial, sans-serif;
    color: var(--ink);
    position: relative;
  }
  .card {
    position: absolute;
    left: 335px;
    width: 530px;
    height: 303px;
    border-radius: 30px;
    overflow: hidden;
  }
  .card--front { top: 125px; background: var(--paper); }
  .card--back  { top: 472px; }

  .brand {
    position: absolute;
    left: 56px; top: 28px;
    display: flex; align-items: center; gap: 18px;
  }
  .brand__mark { width: 62px; height: 62px; background: var(--orange); }
  .brand__name {
    font-weight: 700; color: var(--charcoal); line-height: 1;
  }
  .brand__word { display: block; font-size: 54px; letter-spacing: 1px; }
  .brand__sub { display: block; font-size: 17.5px; letter-spacing: 10.4px; margin-top: 6px; }

  .person {
    position: absolute; left: 0; right: 0; top: 176px; text-align: center;
  }
  .person__name {
    font-size: 21px; font-weight: 500; color: var(--orange); letter-spacing: 0.2px;
  }
  .person__role {
    position: relative; margin-top: 2px; font-size: 12px; line-height: 16px;
  }
  .person__role::before, .person__role::after {
    content: ""; position: absolute; top: 8px; height: 1.5px; background: var(--orange);
  }
  .person__role::before { left: 20px; width: 187px; }
  .person__role::after { right: 20px; width: 188px; }

  .contact {
    position: absolute; left: 20px; top: 222px; list-style: none;
    font-size: 12.5px; line-height: 20px;
  }
  .contact li { display: flex; align-items: center; gap: 3px; }
  .contact svg { width: 11px; height: 11px; fill: var(--orange); }

  .address {
    position: absolute; right: 23px; top: 244px; text-align: right;
    font-size: 12.5px; line-height: 21px; font-style: normal;
  }

  .back__pattern {
    position: absolute; inset: 0;
    background: linear-gradient(135deg, var(--orange) 0%, var(--orange-deep) 100%);
  }
  .back__brand {
    position: absolute; right: 30px; bottom: 58px;
    color: var(--paper); font-size: 20px; font-weight: 700; line-height: 1;
  }
</style>
</head>
<body>
  <section class="card card--front">
    <div class="brand">
      <span class="brand__mark"></span>
      <span class="brand__name">
        <span class="brand__word">VORNEL</span>
        <span class="brand__sub">TECHNOLOGIES</span>
      </span>
    </div>

    <div class="person">
      <div class="person__name">DARREN HOLT</div>
      <div class="person__role">Managing Director</div>
    </div>

    <ul class="contact">
      <li>
        <svg viewBox="0 0 24 24"><path d="M6.6 10.8a15.1 15.1 0 0 0 6.6 6.6l2.2-2.2a1 1 0 0 1 1-.25 11.4 11.4 0 0 0 3.6.57 1 1 0 0 1 1 1V20a1 1 0 0 1-1 1A17 17 0 0 1 3 4a1 1 0 0 1 1-1h3.5a1 1 0 0 1 1 1c0 1.25.2 2.45.57 3.57a1 1 0 0 1-.25 1z"/></svg>
        555 014 2273
      </li>
      <li>
        <svg viewBox="0 0 24 24"><path d="M2 5h20v2l-10 6L2 7zm0 4 10 6 10-6v10H2z"/></svg>
        info@vorneltech.com
      </li>
      <li>
        <svg viewBox="0 0 24 24"><circle cx="12" cy="12" r="10"/></svg>
        www.vorneltech.com
      </li>
    </ul>

    <address class="address">
      4180 Marlow Crest Drive<br>
      Easton Bay CA 90417
    </address>
  </section>

  <section class="card card--back">
    <div class="back__pattern" role="img" aria-label="Repeating brand-symbol pattern in tonal orange"></div>
    <div class="back__brand">Vornel</div>
  </section>
</body>
</html>
```